Name card design for KOV mobile accessories company

KOV is an upmarket brand, we are looking for professional business card design.

the design should be neat and simple but giving a strong feeling.
should not be colorful. make it black/white/gray tone

Name:
Job title:
Contact no.:
company address: i would like the company address to be very small and thin.
link to social media profile:
company website:

*the company have no website yet
as the project is done please i also would like the font that use in design as well; for more further people in company need a business card:)
Updates

Thank you for all super fast submission :D they're all look cool!

i have just update my brief to make the statement clearer, please check it out :)
if you have any question please dont hesitate to ask.
i would like see more design from you! 
Keep it up!  :D

Target Market(s)

Company target are upmarket company distributor, such as Vordane and Pilto store.

Industry/Entity Type

Business

Font styles to use
Serif
Sans Serif
Other font styles liked:
• Formal and mordern

Colors
ffffff
eeeeee
d3d3d3
919191
474747
1b1b1b
000000
333333

Requirements
Must have
• The design must be professional clean and clear but also Strong and Modern!
text should be formal and mordern
Should not have
• No complicated design!

```html
<!DOCTYPE html>
<html lang="en">
<head>
<meta charset="utf-8">
<title>KOV Business Card</title>
<link rel="stylesheet" href="https://fonts.googleapis.com/css2?family=Nunito+Sans:wght@300;400;600&family=Source+Sans+3:wght@600&display=swap">
<style>
  :root {
    --card-black: #1b1a1f;
    --white: #ffffff;
    --light: #eeeeee;
    --soft: #d3d3d3;
    --mid: #919191;
    --dim: #6c6c70;
    --label: #c6c6c6;
    --stage-top: #ffffff;
    --stage-bottom: #ebebeb;
  }
  * { margin: 0; padding: 0; box-sizing: border-box; }
  html, body { width: 1200px; height: 1000px; overflow: hidden; }
  body {
    position: relative;
    background: linear-gradient(160deg, var(--stage-bottom) 0%, var(--stage-top) 45%, var(--stage-bottom) 100%);
    font-family: "Nunito Sans", Arial, sans-serif;
  }
  .card {
    position: absolute;
    width: 798px;
    height: 455px;
    background: var(--card-black);
    box-shadow: 4px 5px 8px rgba(0,0,0,0.25);
  }
  .card--front { left: 40px; top: 30px; }
  .card--back { left: 357px; top: 513px; }
  .abs { position: absolute; white-space: nowrap; }

  .brand-name {
    left: 70px; top: 28px;
    font-size: 150px; font-weight: 600; line-height: 1;
    letter-spacing: 6px; color: var(--white);
  }
  .person-name { left: 72px; top: 239px; font-size: 27px; font-weight: 400; color: var(--white); letter-spacing: 0.5px; }
  .job-title { left: 72px; top: 275px; font-size: 15px; font-weight: 300; color: var(--dim); }
  .email { left: 72px; top: 333px; font-size: 22px; font-weight: 400; color: var(--white); }
  .address { left: 75px; top: 390px; font-size: 17px; font-weight: 300; color: var(--dim); }
  .phone-label { font-size: 16px; font-weight: 300; color: var(--dim); }
  .phone-number { font-size: 23px; font-weight: 400; color: var(--white); letter-spacing: 0.5px; }
  .phone--cell { left: 477px; top: 333px; }
  .phone--fax { left: 477px; top: 384px; }
  .phone .phone-label { margin-right: 10px; }

  .website {
    left: 0; width: 100%; top: 160px; text-align: center;
    font-size: 33px; font-weight: 300; letter-spacing: 6px; color: var(--dim);
  }
  .social { left: 273px; display: flex; align-items: center; gap: 11px; }
  .social--first { top: 240px; }
  .social--second { top: 303px; }
  .social-mark { width: 32px; height: 32px; border-radius: 4px; background: var(--dim); }
  .social-handle { font-size: 22px; font-weight: 400; color: var(--soft); letter-spacing: 0.5px; }

  .side-label {
    position: absolute;
    font-family: "Source Sans 3", Arial, sans-serif;
    font-weight: 600; font-size: 34px; line-height: 45px;
    color: var(--label);
  }
  .side-label--front { left: 865px; top: 193px; }
  .side-label--back { right: 872px; top: 733px; text-align: right; }
</style>
</head>
<body>
  <section class="card card--front">
    <div class="abs brand-name">KOV</div>
    <div class="abs person-name">NAME LAST NAME</div>
    <div class="abs job-title">Job Title</div>
    <div class="abs email">name@kovmail.com</div>
    <div class="abs address">000 Street, City, ST, 00000</div>
    <div class="abs phone phone--cell"><span class="phone-label">C</span><span class="phone-number">888.888.8888</span></div>
    <div class="abs phone phone--fax"><span class="phone-label">F</span><span class="phone-number">888.888.8888</span></div>
  </section>

  <div class="side-label side-label--front">FRONT<br>BUSINESS CARD</div>

  <section class="card card--back">
    <div class="abs website">www.kovsite.com</div>
    <div class="abs social social--first"><span class="social-mark"></span><span class="social-handle">facelink.com/KOV</span></div>
    <div class="abs social social--second"><span class="social-mark"></span><span class="social-handle">chirper.com/KOV</span></div>
  </section>

  <div class="side-label side-label--back">BACK<br>BUSINESS CARD</div>
</body>
</html>
```